Business Card needed for Drainora, a growing Septic Service company

Drainora, a growing local septic service company in Pennsylvania, needs updated business cards. We'd like the business card to feature our logo and communicate that we provide Septic Pumping, Installations/Repairs, Restroom Rentals, and 24/7 Emergency Service. The business card should be eye-catching, bold, and clean/simple. We have been in business almost 10 years and would like to expand and update our business brand and image.

Target Market(s)

Residential and Commercial, New and Current Homeowners

Industry/Entity Type

Service

Contact Information for Business Card

Contact on the business card should be: Dale Pruitt Owner & Operator
Phone: 610-555-0187
Email: service@drainora.example
Website: www.drainora.example
Address: 812 Birchwell Lane Easton PA 18042

Font styles to use
Sans Serif

Colors

Designer to choose colors to be used in the design.

Requirements
Must have
• Feature logo on both side of business card.
Nice to have
• We envision the contact information on one side and our services listed on the other side. Utilize the green from the symbol in our logo as part of the design, overall design color scheme should be white, grey, black.

```html
<!DOCTYPE html>
<html lang="en">
<head>
<meta charset="utf-8">
<title>Drainora Business Card</title>
<link rel="stylesheet" href="https://fonts.googleapis.com/css2?family=Archivo:wght@400;500;800;900&display=swap">
<style>
  :root {
    --stage: #2b2b2b;
    --paper: #ffffff;
    --ink: #111111;
    --grey: #8a8a8a;
    --green: #7dc242;
    --green-light: #8fd04e;
    --green-dark: #6aac34;
  }
  * { box-sizing: border-box; margin: 0; padding: 0; }
  html, body { width: 1200px; height: 1108px; overflow: hidden; }
  body {
    background: var(--stage);
    font-family: "Archivo", Arial, sans-serif;
    position: relative;
  }
  .card {
    position: absolute;
    top: 204px;
    width: 400px;
    height: 700px;
    border-radius: 22px;
    overflow: hidden;
  }
  .card-front { left: 150px; background: var(--paper); color: var(--ink); text-align: center; }
  .card-back { left: 650px; background: var(--green); color: var(--paper); text-align: center; }

  .brand {
    position: absolute;
    top: 150px;
    left: 0; right: 0;
    display: flex;
    align-items: center;
    justify-content: center;
    gap: 14px;
  }
  .brand-square { width: 46px; height: 46px; background: var(--green); }
  .brand-name {
    font-weight: 900;
    font-size: 46px;
    letter-spacing: 1px;
    text-transform: uppercase;
    color: var(--ink);
  }

  .person { position: absolute; top: 392px; left: 0; right: 0; }
  .person-name {
    font-weight: 900;
    font-size: 30px;
    letter-spacing: 2px;
    color: var(--green);
    text-transform: uppercase;
  }
  .person-title { font-size: 18px; margin-top: 2px; }

  .icon-row {
    position: absolute;
    top: 472px;
    left: 0; right: 0;
    display: flex;
    align-items: center;
    justify-content: center;
    gap: 6px;
  }
  .icon-row .rule { width: 36px; height: 1px; background: var(--grey); margin: 0 6px; }
  .icon {
    width: 32px; height: 32px;
    border-radius: 6px;
    background: var(--green);
    display: flex; align-items: center; justify-content: center;
  }

  .contact { position: absolute; top: 524px; left: 0; right: 0; font-size: 17px; line-height: 25px; }
  .contact .accent { color: var(--green); }
  .divider { position: absolute; top: 610px; left: 90px; right: 90px; height: 1px; background: var(--grey); }
  .address { position: absolute; top: 622px; left: 0; right: 0; font-size: 17px; line-height: 24px; }

  .pattern-field {
    position: absolute; inset: 0;
    background: linear-gradient(160deg, var(--green-light) 0%, var(--green) 55%, var(--green-dark) 100%);
  }
  .back-brand {
    position: absolute;
    top: 330px; left: 0; right: 0;
    display: flex; align-items: center; justify-content: center; gap: 12px;
  }
  .back-brand .brand-square { background: var(--paper); width: 38px; height: 38px; }
  .back-brand .brand-name { color: var(--paper); font-size: 32px; }
  .services {
    position: absolute;
    top: 480px; left: 0; right: 0;
    list-style: none;
    font-size: 19px;
    font-weight: 500;
    line-height: 30px;
    text-transform: uppercase;
    letter-spacing: 0.5px;
  }
</style>
</head>
<body>
  <section class="card card-front">
    <div class="brand">
      <span class="brand-square"></span>
      <span class="brand-name">Drainora</span>
    </div>

    <div class="person">
      <div class="person-name">Dale Pruitt</div>
      <div class="person-title">Owner &amp; Operator</div>
    </div>

    <div class="icon-row">
      <span class="rule"></span>
      <span class="icon" aria-label="Phone">
        <svg width="18" height="18" viewBox="0 0 24 24"><path fill="#fff" d="M6.6 10.8a15 15 0 0 0 6.6 6.6l2.2-2.2a1 1 0 0 1 1-.25 11.4 11.4 0 0 0 3.6.57 1 1 0 0 1 1 1V20a1 1 0 0 1-1 1A17 17 0 0 1 3 4a1 1 0 0 1 1-1h3.5a1 1 0 0 1 1 1c0 1.25.2 2.45.57 3.57a1 1 0 0 1-.25 1z"/></svg>
      </span>
      <span class="icon" aria-label="Email">
        <svg width="18" height="18" viewBox="0 0 24 24"><rect x="3" y="6" width="18" height="12" fill="none" stroke="#fff" stroke-width="2"/><path d="M3 6l9 7 9-7" fill="none" stroke="#fff" stroke-width="2"/></svg>
      </span>
      <span class="icon" aria-label="Website">
        <svg width="18" height="18" viewBox="0 0 24 24"><circle cx="12" cy="12" r="8.5" fill="none" stroke="#fff" stroke-width="2"/><path d="M3.5 12h17M12 3.5c3 3 3 14 0 17M12 3.5c-3 3-3 14 0 17" fill="none" stroke="#fff" stroke-width="1.5"/></svg>
      </span>
      <span class="rule"></span>
    </div>

    <div class="contact">
      <div>610-555-0187</div>
      <div>service@drainora.example</div>
      <div>www.<span class="accent">drainora</span>.example</div>
    </div>
    <div class="divider"></div>
    <div class="address">
      <div>812 Birchwell Lane</div>
      <div>Easton PA 18042</div>
    </div>
  </section>

  <section class="card card-back">
    <div class="pattern-field" role="img" aria-label="Tonal green background pattern of repeated brand tiles"></div>
    <div class="back-brand">
      <span class="brand-square"></span>
      <span class="brand-name">Drainora</span>
    </div>
    <ul class="services">
      <li>Septic Pumping</li>
      <li>Installations/Repairs</li>
      <li>Restroom Rentals</li>
      <li>24/7 Emergency Service</li>
    </ul>
  </section>
</body>
</html>
```